Consultant Word Template Design

I want to use a word template to submit service proposals to clients. You can visit my web site: Brightwayadvisory.com for content/ design ideas and I am also attaching my flyer. The color scheme should be consistent with my logo, web, flyer, etc. blue and white. I want some core pages: front & back page design, about us, services

Industry/Entity Type

Health Care

Colors

Designer to choose colors to be used in the design.

```html
<!DOCTYPE html>
<html lang="en">
<head>
<meta charset="UTF-8">
<title>Brightway Advisory – Proposal Cover</title>
<link href="https://fonts.googleapis.com/css2?family=Crimson+Text:wght@400;600&display=swap" rel="stylesheet">
<style>
  :root {
    --page-white: #ffffff;
    --brand-blue: #2f5fb3;
    --brand-blue-deep: #24499a;
    --brand-blue-soft: #5a86cc;
    --accent-sky: #2aa6dc;
    --text-light: #ffffff;
    --brand-text: #1f4e9c;
  }
  * { margin: 0; padding: 0; box-sizing: border-box; }
  html, body {
    width: 901px;
    height: 1200px;
    overflow: hidden;
    background: var(--page-white);
  }
  .cover {
    position: relative;
    width: 901px;
    height: 1200px;
    background: var(--page-white);
    font-family: "Crimson Text", Georgia, serif;
  }
  .cover-art {
    position: absolute;
    inset: 0;
    width: 901px;
    height: 1200px;
    display: block;
  }
  .brand {
    position: absolute;
    top: 262px;
    left: 0;
    width: 100%;
    display: flex;
    justify-content: center;
    align-items: center;
    gap: 16px;
  }
  .brand-dot {
    width: 26px;
    height: 26px;
    border-radius: 50%;
    background: var(--brand-text);
  }
  .brand-name {
    font-weight: 600;
    font-size: 38px;
    letter-spacing: 1px;
    color: var(--brand-text);
  }
  .cover-titles {
    position: absolute;
    top: 740px;
    left: 0;
    width: 100%;
    text-align: center;
    color: var(--text-light);
  }
  .product-title {
    font-weight: 400;
    font-size: 72px;
    line-height: 1.1;
  }
  .product-subtitle {
    margin-top: 4px;
    font-weight: 600;
    font-size: 55px;
    line-height: 1.1;
  }
</style>
</head>
<body>
  <main class="cover">
    <svg class="cover-art" viewBox="0 0 901 1200" xmlns="http://www.w3.org/2000/svg">
      <defs>
        <linearGradient id="photoBase" x1="0" y1="0" x2="0" y2="1">
          <stop offset="0" stop-color="#4573c0"/>
          <stop offset="0.45" stop-color="#3563b4"/>
          <stop offset="1" stop-color="#2a53a2"/>
        </linearGradient>
        <radialGradient id="photoGlowLeft" cx="0.22" cy="0.35" r="0.45">
          <stop offset="0" stop-color="#7ea2da" stop-opacity="0.55"/>
          <stop offset="1" stop-color="#7ea2da" stop-opacity="0"/>
        </radialGradient>
        <radialGradient id="photoGlowRight" cx="0.78" cy="0.42" r="0.4">
          <stop offset="0" stop-color="#6d94d2" stop-opacity="0.45"/>
          <stop offset="1" stop-color="#6d94d2" stop-opacity="0"/>
        </radialGradient>
        <radialGradient id="photoShade" cx="0.5" cy="1" r="0.6">
          <stop offset="0" stop-color="#1f418a" stop-opacity="0.5"/>
          <stop offset="1" stop-color="#1f418a" stop-opacity="0"/>
        </radialGradient>
        <clipPath id="panelClip">
          <path d="M0 522 Q450 356 901 494 L901 1200 L0 1200 Z"/>
        </clipPath>
      </defs>
      <path class="accent-arc" d="M0 498 Q450 330 901 470" fill="none" stroke="var(--accent-sky)" stroke-width="14"/>
      <g class="photo-panel" role="img" aria-label="Photo of healthcare professionals meeting around a table, tinted in brand blue" clip-path="url(#panelClip)">
        <rect x="0" y="350" width="901" height="850" fill="url(#photoBase)"/>
        <rect x="0" y="350" width="901" height="850" fill="url(#photoGlowLeft)"/>
        <rect x="0" y="350" width="901" height="850" fill="url(#photoGlowRight)"/>
        <rect x="0" y="350" width="901" height="850" fill="url(#photoShade)"/>
      </g>
    </svg>

    <div class="brand">
      <span class="brand-dot"></span>
      <span class="brand-name">Brightway Advisory LLC</span>
    </div>

    <div class="cover-titles">
      <h1 class="product-title">Product Title here</h1>
      <p class="product-subtitle">Subtitle here</p>
    </div>
  </main>
</body>
</html>
```